Business logo & card design needed

We need a business logo & card design for a new company in NSW called 'Kestrel Solutions'.
The company provides electrical services such as; electrical/refrigeration & air conditioning/data/security/audio visual entertainment/design & install.
We would like a logo which can relate to the electrical industry.

Reason: Have not found a design I like

Industry/Entity Type

Electrical

Contact Information for Business Card

Kestrel Solutions
Tomas Velkovic, Ph: 0471936058, Lic: 502967F

Logo Text

Kestrel Solutions

Logo styles of interest
Emblem Logo
Abstract Logo
Wordmark Logo
Requirements
Must have
• The card must include the services we provide; electrical/refrigeration & air conditioning/data/security/audio visual entertainment/design & install.
It must also include the licence number; Lic: 502967F

```html
<!DOCTYPE html>
<html lang="en">
<head>
<meta charset="utf-8">
<title>Kestrel Solutions – Business Card</title>
<link rel="stylesheet" href="https://fonts.googleapis.com/css2?family=Alegreya:wght@400&display=swap">
<style>
  :root {
    --page-bg: #e9e9e9;
    --card-bg: #ffffff;
    --brand-blue: #4a9cd9;
    --rule-blue: #5aa6de;
    --accent-orange: #f08a24;
  }
  html, body {
    margin: 0;
    padding: 0;
    width: 1200px;
    height: 750px;
    overflow: hidden;
    background: var(--page-bg);
  }
  .business-card {
    position: absolute;
    left: 120px;
    top: 97px;
    width: 960px;
    height: 556px;
    background: var(--card-bg);
    box-shadow: 0 6px 18px rgba(0, 0, 0, 0.18);
    font-family: "Alegreya", Georgia, serif;
    color: var(--brand-blue);
  }
  .brand {
    position: absolute;
    left: 64px;
    top: 62px;
    display: flex;
    align-items: flex-start;
    gap: 10px;
  }
  .brand-mark {
    width: 30px;
    height: 30px;
    margin-top: 18px;
  }
  .brand-name {
    margin: 0;
    font-weight: 400;
    font-size: 52px;
    line-height: 42px;
    letter-spacing: -0.5px;
    color: var(--brand-blue);
  }
  .brand-name span { display: block; }
  .divider-rule {
    position: absolute;
    left: 65px;
    top: 184px;
    width: 826px;
    height: 1.5px;
    background: var(--rule-blue);
  }
  .contact {
    position: absolute;
    right: 69px;
    top: 126px;
    text-align: right;
  }
  .contact-name {
    margin: 0;
    font-size: 44px;
    line-height: 52px;
    font-weight: 400;
  }
  .contact-phone {
    margin: 8px 0 0;
    font-size: 20px;
    line-height: 24px;
  }
  .services {
    position: absolute;
    left: 65px;
    top: 348px;
    margin: 0;
    font-size: 23px;
    line-height: 35px;
  }
  .services span { display: block; }
</style>
</head>
<body>
  <article class="business-card">
    <header class="brand">
      <svg class="brand-mark" viewBox="0 0 30 30" aria-hidden="true">
        <circle cx="15" cy="15" r="14" fill="var(--accent-orange)"/>
      </svg>
      <h1 class="brand-name"><span>Kestrel</span><span>Solutions</span></h1>
    </header>

    <div class="divider-rule"></div>

    <section class="contact">
      <p class="contact-name">Tomas Velkovic</p>
      <p class="contact-phone">P: 0471936058</p>
    </section>

    <p class="services">
      <span>The card must include the services we provide;</span>
      <span>electrical/refrigeration &amp; air conditioning/</span>
      <span>data/security/audio visual entertainment/design &amp; install</span>
      <span>Licence number: Lic: 502967F</span>
    </p>
  </article>
</body>
</html>
```